8 behaviours infographic

We are a portfolio of approx. 200 resources in technology within a financial services enterprise (5000-6000 employees).
Our portfolio name is Harbour and Planner Asset Services.
Our leadership team has collectively defined a set of 8 behaviours that represent how we should behave and interact amongst ourselves.
We need an infographic that can bring these behaviours to life and be displayed around the workplace on large posters where teams work (the words for the behaviours should also be incorporated into the infographic).
We have also included our team's logo, which needs to be incorporated into the infographic.
The 8 behaviours are:
- Listen & show you care
- Support Each Other
- Be Accountable
- Communicate openly
- Collaborate and leverage the collective strength of the group
- Influence the agenda
- Proactive deliberate and team focussed
- Celebrate success & have fun
Look and feel
Each slider illustrates characteristics of the customer's brand and the style your logo design should communicate.

```html
<!DOCTYPE html>
<html lang="en">
<head>
<meta charset="utf-8">
<title>Harbour and Planner Asset Services – 8 Behaviours</title>
<link rel="stylesheet" href="https://fonts.googleapis.com/css2?family=Montserrat:wght@500;800;900&family=Pacifico&display=swap">
<style>
  :root{
    --blue:#1b75bb;
    --blue-light:#cfe2f3;
    --ink:#231f20;
    --white:#ffffff;
    --grey-light:#efefef;
    --grey-mid:#d6d6d6;
    --grey-dark:#4a4a4a;
    --orange:#f7941d;
    --silhouette:#3a3a3a;
  }
  *{margin:0;padding:0;box-sizing:border-box}
  html,body{width:1200px;height:4712px;overflow:hidden;background:var(--white)}
  .poster{position:relative;width:1200px;height:4712px;background:var(--white);
    font-family:"Montserrat",Arial,sans-serif;font-weight:800;color:var(--ink);overflow:hidden}
  .abs{position:absolute}
  .line{position:absolute;white-space:nowrap;line-height:1;text-transform:uppercase}
  .blue{color:var(--blue)}
  .ink{color:var(--ink)}
  .white{color:var(--white)}
  .right{text-align:right}
  .art{position:absolute}

  /* header */
  .team-name{position:absolute;left:0;top:40px;width:1200px;text-align:center;
    font-size:44px;line-height:1.15;font-weight:800;color:var(--ink)}
  .big-eight{position:absolute;left:40px;top:150px;font-size:300px;line-height:1;font-weight:900;color:var(--blue)}
  .title-band{position:absolute;left:200px;top:283px;width:962px;height:110px;background:var(--blue)}
  .title-band span{position:absolute;left:60px;top:8px;font-size:98px;line-height:1;font-weight:900;
    letter-spacing:8px;color:var(--white)}

  /* section backgrounds */
  .bg-support{position:absolute;left:0;top:980px;width:1200px;height:528px;
    background:linear-gradient(180deg,#e4e4e4,var(--grey-mid))}
  .bg-communicate{position:absolute;left:0;top:2073px;width:1200px;height:472px;background:var(--grey-light)}
  .bg-collaborate{position:absolute;left:0;top:2560px;width:1200px;height:487px;background:var(--grey-dark)}
  .bg-celebrate{position:absolute;left:0;top:4005px;width:1200px;height:707px;
    background:linear-gradient(180deg,var(--grey-light),var(--grey-mid))}

  .accountable-band{position:absolute;left:0;top:1885px;width:1200px;height:157px;background:var(--blue)}
  .openly-box{position:absolute;left:612px;top:2208px;width:535px;height:117px;background:var(--blue)}

  .collab-intro{position:absolute;left:57px;font-size:60px;line-height:1;font-weight:500;color:var(--white);white-space:nowrap}
  .collab-strong{color:var(--orange);font-size:60px;font-weight:900}

  .celebrate-word{position:absolute;left:0;top:4060px;width:1200px;text-align:center;
    font-family:"Pacifico",cursive;font-size:170px;line-height:1.2;color:var(--blue);font-weight:400}
  .celebrate-sub{position:absolute;left:0;top:4282px;width:1200px;text-align:center;
    font-size:44px;line-height:1;font-weight:900;color:var(--ink);text-transform:uppercase}
</style>
</head>
<body>
<main class="poster">

  <!-- header -->
  <div class="team-name">Harbour and Planner<br>Asset Services</div>
  <div class="title-band"><span>BEHAVIOURS</span></div>
  <div class="big-eight">8</div>

  <!-- 1 listen -->
  <svg class="art" style="left:0;top:440px" width="540" height="500" role="img" aria-label="Blue silhouette of a woman watering a small plant held in a large open hand">
    <defs><linearGradient id="g-listen" x1="0" y1="0" x2="1" y2="1"><stop offset="0" stop-color="#dbe9f6"/><stop offset="1" stop-color="#5b9bd0"/></linearGradient></defs>
    <rect width="540" height="500" fill="url(#g-listen)"/>
  </svg>
  <div class="line ink" style="left:580px;top:550px;font-size:86px;font-weight:900">Listen &amp;</div>
  <div class="line blue" style="left:575px;top:630px;font-size:160px;font-weight:900">Show</div>
  <div class="line ink" style="left:580px;top:785px;font-size:86px;font-weight:900">You care</div>

  <!-- 2 support -->
  <div class="bg-support"></div>
  <svg class="art" style="left:0;top:1240px" width="680" height="268" role="img" aria-label="Grey mountain range silhouettes">
    <rect width="680" height="268" fill="#9a9a9a"/>
  </svg>
  <svg class="art" style="left:675px;top:1005px" width="525" height="503" role="img" aria-label="Dark silhouettes of climbers helping each other up a rocky peak">
    <defs><linearGradient id="g-climb" x1="0" y1="0" x2="0" y2="1"><stop offset="0" stop-color="#6a6a6a"/><stop offset="1" stop-color="var(--silhouette)"/></linearGradient></defs>
    <rect width="525" height="503" fill="url(#g-climb)"/>
  </svg>
  <div class="line blue" style="left:57px;top:1037px;font-size:112px;font-weight:900">Support</div>
  <div class="line ink" style="left:57px;top:1153px;font-size:72px;font-weight:900">Each other</div>

  <!-- 3 accountable -->
  <svg class="art" style="left:0;top:1540px" width="1200" height="345" role="img" aria-label="Blue silhouette landscape with trees, birds and a father kneeling to hand a cup to a child">
    <defs><linearGradient id="g-acc" x1="0" y1="0" x2="0" y2="1"><stop offset="0" stop-color="#e3eef8"/><stop offset="1" stop-color="#4f90c8"/></linearGradient></defs>
    <rect width="1200" height="345" fill="url(#g-acc)"/>
  </svg>
  <div class="accountable-band"></div>
  <div class="line white" style="left:57px;top:1912px;font-size:104px;font-weight:900">Be accountable</div>

  <!-- 4 communicate -->
  <div class="bg-communicate"></div>
  <svg class="art" style="left:47px;top:2090px" width="770" height="455" role="img" aria-label="Speech bubbles above dark silhouettes of people seated around a meeting table">
    <defs><linearGradient id="g-comm" x1="0" y1="0" x2="0" y2="1"><stop offset="0" stop-color="#dcdcdc"/><stop offset="1" stop-color="#3f3f3f"/></linearGradient></defs>
    <rect width="770" height="455" fill="url(#g-comm)"/>
  </svg>
  <div class="line ink right" style="left:560px;top:2136px;width:587px;font-size:66px;font-weight:900">Communicate</div>
  <div class="openly-box"></div>
  <div class="line white right" style="left:612px;top:2214px;width:520px;font-size:108px;font-weight:900">Openly</div>

  <!-- 5 collaborate -->
  <div class="bg-collaborate"></div>
  <div class="collab-intro" style="top:2607px">Collaborate</div>
  <div class="collab-intro" style="top:2690px">and leverage</div>
  <div class="line collab-strong" style="left:57px;top:2796px">The collective</div>
  <div class="line collab-strong" style="left:57px;top:2864px">strength of</div>
  <div class="line collab-strong" style="left:57px;top:2932px">the group</div>
  <svg class="art" style="left:720px;top:2590px" width="458" height="430" role="img" aria-label="Top-down view of people seated around a round table working together">
    <rect width="458" height="430" fill="#8c8c8c"/>
  </svg>

  <!-- 6 influence -->
  <svg class="art" style="left:31px;top:3094px" width="723" height="361" role="img" aria-label="Sketch of a cyclist leading two riders in the distance">
    <rect width="723" height="361" fill="#c9c9c9"/>
  </svg>
  <div class="line blue right" style="left:560px;top:3094px;width:587px;font-size:96px;font-weight:900">Influence</div>
  <div class="line ink right" style="left:560px;top:3204px;width:587px;font-size:62px;font-weight:800">The agenda</div>

  <!-- 7 proactive -->
  <div class="line blue right" style="left:100px;top:3530px;width:670px;font-size:90px;font-weight:900">Proactive</div>
  <div class="line blue right" style="left:100px;top:3632px;width:670px;font-size:90px;font-weight:900">Deliberate</div>
  <div class="line ink right" style="left:100px;top:3734px;width:670px;font-size:90px;font-weight:900">and team</div>
  <div class="line ink right" style="left:100px;top:3836px;width:670px;font-size:90px;font-weight:900">focussed</div>
  <svg class="art" style="left:800px;top:3480px" width="347" height="480" role="img" aria-label="Blue silhouette of an archer drawing a bow">
    <defs><linearGradient id="g-arch" x1="0" y1="0" x2="0" y2="1"><stop offset="0" stop-color="#cfe2f3"/><stop offset="1" stop-color="#1b75bb"/></linearGradient></defs>
    <rect width="347" height="480" fill="url(#g-arch)"/>
  </svg>

  <!-- 8 celebrate -->
  <div class="bg-celebrate"></div>
  <div class="celebrate-word">Celebrate</div>
  <div class="celebrate-sub">Success &amp; have fun</div>
  <svg class="art" style="left:0;top:4335px" width="1200" height="377" role="img" aria-label="Dark silhouette of a cheering crowd with raised arms">
    <defs><linearGradient id="g-crowd" x1="0" y1="0" x2="0" y2="1"><stop offset="0" stop-color="#bdbdbd"/><stop offset="1" stop-color="#262626"/></linearGradient></defs>
    <rect width="1200" height="377" fill="url(#g-crowd)"/>
  </svg>

</main>
</body>
</html>
```